Brivolan - presentation for a remote DBA team offering data platform management

We need a website design for wordpress site called Brivolan.cz
We deliver remote database and data platform administration and development, oversee the database administrators, consult and train the personnel responsible for the database operations. The website should include several sections, home page with graphics elements supporting the name and service - remote dba work; blog section; service introduction and description, team introduction and description, download section for documents, presentations etc.

Target Market(s)

small and medium business companies requiring remote DBA service

Number of Pages Required

3 page

Font styles to use
Sans Serif

Colors

Designer to choose colors to be used in the design.

Requirements
Must have
• The website should have several sections to introduce the services, blog, team introduction, downloads

```html
<!DOCTYPE html>
<html lang="en">
<head>
<meta charset="utf-8">
<title>Brivolan.cz – Remote Database Administration</title>
<link rel="stylesheet" href="https://fonts.googleapis.com/css2?family=Roboto:wght@300;400;500;700;900&family=Oswald:wght@400;500&display=swap">
<style>
:root{
  --blue:#22b5e5;
  --blue-dark:#1a9ccb;
  --ink:#1e1e1e;
  --text:#555;
  --light:#f0f0f0;
  --footer:#262626;
  --white:#fff;
}
*{box-sizing:border-box;margin:0;padding:0}
html,body{width:1200px;height:3220px;overflow:hidden}
body{position:relative;font-family:'Roboto',sans-serif;color:var(--text);background:var(--white)}
.abs{position:absolute}
p{font-size:12.5px;line-height:1.55}

/* header */
.site-header{top:0;left:0;width:1200px;height:72px;background:var(--white)}
.brand{left:172px;top:20px;font:900 27px 'Roboto',sans-serif;color:var(--ink);letter-spacing:.3px}
.brand span{color:var(--blue)}
.main-nav{right:168px;top:0;height:72px;display:flex;align-items:center}
.main-nav a{font-size:13px;color:var(--ink);text-decoration:none;padding:0 16px;border-left:1px solid #ddd;line-height:72px}
.main-nav a:first-child{border-left:none}

/* hero */
.hero{top:72px;left:0;width:1200px;height:485px;background:linear-gradient(90deg,#3a3e44 0%,#a8adb3 30%,#e4e6e8 50%,#a8adb3 70%,#3a3e44 100%)}
.hero-title{top:258px;left:0;width:1200px;text-align:center;font:500 41px/1.2 'Oswald',sans-serif;color:var(--white);text-transform:uppercase;text-shadow:0 2px 6px rgba(0,0,0,.35)}
.hero-sub{top:320px;left:404px;width:418px;height:34px;background:rgba(60,60,60,.85);color:var(--white);font:400 14px/34px 'Oswald',sans-serif;text-align:center;text-transform:uppercase;white-space:nowrap;letter-spacing:.2px}

/* services */
.service{top:599px;width:277px;height:290px;background:var(--blue);text-align:center;color:var(--white)}
.service .thumb{height:146px}
.service h3{font-size:15px;font-weight:700;text-transform:uppercase;margin-top:12px}
.service p{font-size:11px;line-height:1.45;padding:4px 24px 0}
.btn-dark{display:inline-block;background:var(--ink);color:var(--white);font-size:10px;font-weight:700;text-transform:uppercase;padding:10px 18px;margin-top:14px}

/* welcome */
.welcome-art{left:161px;top:945px;width:344px;height:245px}
.welcome{left:524px;top:940px;width:505px}
.welcome h2{font-size:32px;font-weight:300;color:var(--ink)}
.welcome h2 b{font-weight:700}
.welcome p{margin-top:10px;font-size:11.5px;color:#444}
.btn{display:inline-block;font-size:11px;font-weight:500;text-transform:uppercase;padding:12px 20px;color:var(--white)}
.btn.dark{background:var(--ink)}
.btn.blue{background:var(--blue);margin-left:8px}

/* why */
.why-bg{top:1239px;left:0;width:597px;height:429px;background:var(--light)}
.why-photo{top:1239px;left:597px;width:603px;height:429px;background:linear-gradient(120deg,#b9c2ca,#8c969f 45%,#3b3f44)}
.why{left:172px;top:1268px;width:400px}
.why h2{font-size:30px;font-weight:300;color:var(--ink);line-height:1.1}
.why h2 b{display:block;font-weight:900;margin-left:60px}
.why > p{margin-top:14px;font-size:11.5px;color:#333}
.feature{margin-top:14px}
.feature h4{font-size:14px;font-weight:700;color:var(--ink);display:flex;align-items:center;gap:10px}
.feature h4 svg{flex:none}
.feature p{font-size:11.5px;color:#333;margin-top:4px}

/* blog */
.section-title{left:0;width:1200px;text-align:center;font-size:29px;font-weight:900;color:var(--ink);text-transform:uppercase}
.section-title::after{content:"";display:block;width:120px;height:2px;background:#ccc;margin:10px auto 0;box-shadow:inset 40px 0 0 var(--blue),inset -40px 0 0 var(--blue)}
.blog-main{left:161px;top:1797px;width:427px;height:292px;background:linear-gradient(135deg,#c5d3de,#7d8e9c 55%,#46515a)}
.date{position:absolute;left:0;bottom:0;width:52px;height:48px;background:var(--blue);color:var(--white);text-align:center;font-weight:700;font-size:15px;line-height:1.05;padding-top:7px}
.date small{display:block;font-size:13px}
.blog-thumb{left:612px;width:129px;height:120px}
.post{left:758px;width:280px}
.post h3{font-size:13px;font-weight:500;color:var(--ink);text-transform:uppercase}
.post .meta{font-size:10px;color:#888;margin-top:5px}
.post .meta b{font-weight:400;color:var(--ink)}
.post p{font-size:11px;color:#444;margin-top:7px;line-height:1.45}
.post-foot{display:flex;align-items:center;margin-top:10px;font-size:10px;color:#444}
.btn-outline{border:1px solid var(--ink);padding:7px 10px;font-size:9.5px;font-weight:500;text-transform:uppercase;color:var(--ink)}
.post-foot .c{margin-left:auto;display:flex;align-items:center;gap:4px}
.post-foot .l{margin-left:20px;display:flex;align-items:center;gap:4px}
.divider{left:612px;top:1945px;width:426px;height:1px;background:#ddd}

/* team */
.team-bg{top:2160px;left:0;width:1200px;height:650px;background:linear-gradient(#e6e6e6,#f1f1f1)}
.team-intro{left:230px;top:2258px;width:740px;text-align:center;font-size:11px;color:#333}
.member{top:2308px;width:259px;text-align:center}
.member .portrait{height:279px;margin:0 auto;width:210px;background:linear-gradient(#e6e6e6,#5c636b 70%,#2d3136)}
.member .card{background:var(--blue);height:159px;color:var(--white);padding-top:22px;border-bottom:5px solid var(--blue-dark)}
.member h3{font-size:15px;font-weight:700;text-transform:uppercase}
.member p{font-size:11px;line-height:1.45;padding:10px 22px 0}
.socials{display:flex;justify-content:center;gap:6px;margin-top:10px}
.socials i{width:24px;height:24px;border:1.5px solid currentColor;border-radius:50%;display:block}

/* footer */
.site-footer{top:2810px;left:0;width:1200px;height:368px;background:var(--footer)}
.subscribe{left:374px;top:2866px;display:flex}
.subscribe .field{width:334px;height:36px;background:var(--white);font-size:10.5px;color:#999;padding:12px 14px}
.subscribe .go{width:108px;height:36px;background:var(--blue);color:var(--white);font-weight:700;font-size:13px;text-align:center;line-height:36px}
.footer-brand{left:0;top:2930px;width:1200px;text-align:center;font-size:26px;font-weight:900;color:var(--white)}
.footer-text{left:228px;top:2982px;width:744px;text-align:center;font-size:10.5px;color:#bbb}
.footer-social{left:0;top:3065px;width:1200px;color:var(--white)}
.contact-row{left:0;top:3122px;width:1200px;display:flex;justify-content:center;gap:70px;font-size:10.5px;color:#ddd}
.contact-row span{display:flex;align-items:center;gap:6px}
.copyright{left:0;top:3178px;width:1200px;height:42px;background:var(--blue);color:var(--white);font-size:11px;text-align:center;line-height:42px}
</style>
</head>
<body>

<header class="site-header abs">
  <div class="brand abs">BRIVOLAN<span>.CZ</span></div>
  <nav class="main-nav abs">
    <a>HOME</a><a>SERVICES</a><a>BLOG</a><a>TEAM</a><a>DOWNLOAD</a><a>CONTACT US</a>
  </nav>
</header>

<section class="hero abs" role="img" aria-label="Photo of a bright data centre corridor lined with server racks"></section>
<h1 class="hero-title abs">We are specialists in data service</h1>
<div class="hero-sub abs">We deliver remote database and data platform administration</div>

<article class="service abs" style="left:161px">
  <div class="thumb" role="img" aria-label="Photo of a businessman touching a cloud network graphic" style="background:linear-gradient(135deg,#dfe9f1,#7f98ad 60%,#2d3c4a)"></div>
  <h3>Remote Database</h3>
  <p>Lorem Ipsum is simply dummy text of the printing and typesetting industry. Lorem Ipsum has text the type and scrambled it to make specimen</p>
  <span class="btn-dark">Read more</span>
</article>
<article class="service abs" style="left:464px">
  <div class="thumb" role="img" aria-label="Photo of server racks under a blue sky" style="background:linear-gradient(#3f8fd6,#cfe4f4 55%,#4f5a63)"></div>
  <h3>Database Administrators</h3>
  <p>Lorem Ipsum is simply dummy text of the printing and typesetting industry. Lorem Ipsum has text the type and scrambled it to make specimen</p>
  <span class="btn-dark">Read more</span>
</article>
<article class="service abs" style="left:762px">
  <div class="thumb" role="img" aria-label="Photo of server towers rising above clouds" style="background:linear-gradient(#5b7d9c,#b7c9d8 60%,#e9eef2)"></div>
  <h3>Data Consult and Training</h3>
  <p>Lorem Ipsum is simply dummy text of the printing and typesetting industry. Lorem Ipsum has text the type and scrambled it to make specimen</p>
  <span class="btn-dark">Read more</span>
</article>

<div class="welcome-art abs" role="img" aria-label="Illustration of server racks inside a blue cloud outline" style="background:radial-gradient(ellipse at 50% 45%,#cfeefa 0%,#7fd0ef 45%,#ffffff 72%)"></div>
<section class="welcome abs">
  <h2>Welcome to <b>Brivolan.cz</b></h2>
  <p>Lorem Ipsum is simply dummy text of the printing and typesetting industry. Lorem Ipsum has been type and scrambled it to make a type specimen book. It has survived not only five centuries, but also the leap into electronic typesetting, remaining essentially unchanged. It was popularised in the 1960s with the release of Letterform sheets containing Lorem Ipsum passages, and more recently with desktop publishing software like Pagewright Studio including versions of Lorem Ipsum.</p>
  <p>Lorem Ipsum is simply dummy text of the printing and typesetting industry. Lorem Ipsum has been with the release of Letterform sheets containing Lorem Ipsum passages, and more recently with desktop publishing software like Pagewright Studio including versions of Lorem Ipsum.</p>
  <div style="margin-top:22px"><span class="btn dark">Learn more</span><span class="btn blue">Get started</span></div>
</section>

<div class="why-bg abs"></div>
<div class="why-photo abs" role="img" aria-label="Photo of an engineer working on a laptop beside server racks"></div>
<section class="why abs">
  <h2>Why choose <b>BRIVOLAN.CZ</b></h2>
  <p>Lorem Ipsum is simply dummy text of the printing and typesetting industry.<br>Lorem Ipsum has been the industry's standard dummy text.</p>
  <div class="feature">
    <h4><svg width="30" height="30" viewBox="0 0 30 30"><rect x="3" y="4" width="9" height="6" fill="#22b5e5"/><rect x="3" y="12" width="9" height="6" fill="#22b5e5"/><rect x="3" y="20" width="9" height="6" fill="#22b5e5"/><rect x="15" y="5" width="12" height="3" fill="#22b5e5"/><rect x="15" y="13" width="12" height="3" fill="#22b5e5"/><rect x="15" y="21" width="12" height="3" fill="#22b5e5"/></svg>Unlimited Features</h4>
    <p>Lorem Ipsum is simply dummy text of the printing and typesetting industry.<br>Lorem Ipsum has been the industry's standard dummy text.</p>
  </div>
  <div class="feature">
    <h4><svg width="30" height="30" viewBox="0 0 30 30"><rect x="3" y="5" width="22" height="16" rx="2" fill="#22b5e5"/><rect x="6" y="14" width="3" height="5" fill="#fff"/><rect x="11" y="10" width="3" height="9" fill="#fff"/><rect x="16" y="12" width="3" height="7" fill="#fff"/><rect x="8" y="23" width="12" height="3" fill="#22b5e5"/></svg>Free data analysis</h4>
    <p>Lorem Ipsum is simply dummy text of the printing and typesetting industry.<br>Lorem Ipsum has been the industry's standard dummy text.</p>
  </div>
  <div class="feature">
    <h4><svg width="30" height="30" viewBox="0 0 30 30"><circle cx="15" cy="10" r="6" fill="#22b5e5"/><path d="M4 27c1-7 6-10 11-10s10 3 11 10z" fill="#22b5e5"/><path d="M7 11a8 8 0 0 1 16 0" stroke="#22b5e5" stroke-width="2" fill="none"/></svg>Free Support</h4>
    <p>Lorem Ipsum is simply dummy text of the printing and typesetting industry.<br>Lorem Ipsum has been the industry's standard dummy text.</p>
  </div>
</section>

<h2 class="section-title abs" style="top:1712px">Latest Blog</h2>
<div class="blog-main abs" role="img" aria-label="Photo of two engineers reviewing a laptop in a server room"><div class="date">15<small>DEC</small></div></div>

<div class="blog-thumb abs" style="top:1797px;background:linear-gradient(#4a90d0,#c9dbe8 60%,#545c63)" role="img" aria-label="Photo of server racks under a blue sky"><div class="date">15<small>DEC</small></div></div>
<article class="post abs" style="top:1797px">
  <h3>Blog heading here</h3>
  <div class="meta">Posted By: <b>Ilsa Norwin</b> on <b>April 5th,2018</b></div>
  <p>Lorem Ipsum is simply dummy text of the printing and typesetting industry. Lorem Ipsum has been the industry</p>
  <div class="post-foot"><span class="btn-outline">Read more ›</span>
    <span class="c"><svg width="11" height="10" viewBox="0 0 11 10"><path d="M1 1h9v6H5l-3 2V7H1z" fill="#22b5e5"/></svg>Comments</span>
    <span class="l"><svg width="11" height="10" viewBox="0 0 11 10"><path d="M5.5 9L1 4.5A2.3 2.3 0 0 1 5.5 2a2.3 2.3 0 0 1 4.5 2.5z" fill="#22b5e5"/></svg>0 Likes</span></div>
</article>
<div class="divider abs"></div>
<div class="blog-thumb abs" style="top:1969px;background:linear-gradient(135deg,#5b86b5,#2c4f78 60%,#1d2f45)" role="img" aria-label="Photo of a hand touching a data management graphic"><div class="date">15<small>DEC</small></div></div>
<article class="post abs" style="top:1969px">
  <h3>Blog heading here</h3>
  <div class="meta">Posted By: <b>Ilsa Norwin</b> on <b>April 5th,2018</b></div>
  <p>Lorem Ipsum is simply dummy text of the printing and typesetting industry. Lorem Ipsum has been the industry</p>
  <div class="post-foot"><span class="btn-outline">Read more ›</span>
    <span class="c"><svg width="11" height="10" viewBox="0 0 11 10"><path d="M1 1h9v6H5l-3 2V7H1z" fill="#22b5e5"/></svg>Comments</span>
    <span class="l"><svg width="11" height="10" viewBox="0 0 11 10"><path d="M5.5 9L1 4.5A2.3 2.3 0 0 1 5.5 2a2.3 2.3 0 0 1 4.5 2.5z" fill="#22b5e5"/></svg>0 Likes</span></div>
</article>

<div class="team-bg abs"></div>
<h2 class="section-title abs" style="top:2200px">Our Team</h2>
<p class="team-intro abs">Lorem Ipsum is simply dummy text of the printing and typesetting industry. Lorem Ipsum has been the industry's standard dummy text ever since the 1500s, when recently with desktop publishing software like Pagewright Studio including versions of Lorem Ipsum.</p>

<article class="member abs" style="left:172px">
  <div class="portrait" role="img" aria-label="Portrait photo of team member in a dark suit"></div>
  <div class="card"><h3>Oren Vaszek</h3><p>Lorem ipsum is simply dummy text of the printing and typesetting industry. Lorem Ipsum has been the industry text...</p><div class="socials"><i></i><i></i><i></i></div></div>
</article>
<article class="member abs" style="left:483px">
  <div class="portrait" role="img" aria-label="Portrait photo of team member in a dark blazer"></div>
  <div class="card"><h3>Marla Quenby</h3><p>Lorem ipsum is simply dummy text of the printing and typesetting industry. Lorem Ipsum has been the industry text...</p><div class="socials"><i></i><i></i><i></i></div></div>
</article>
<article class="member abs" style="left:790px">
  <div class="portrait" role="img" aria-label="Portrait photo of team member in a dark suit"></div>
  <div class="card"><h3>Teodor Halm</h3><p>Lorem ipsum is simply dummy text of the printing and typesetting industry. Lorem Ipsum has been the industry text...</p><div class="socials"><i></i><i></i><i></i></div></div>
</article>

<footer class="site-footer abs"></footer>
<div class="subscribe abs"><div class="field">Enter Your Email Id</div><div class="go">SUBSCRIBE</div></div>
<div class="footer-brand abs">BRIVOLAN.CZ</div>
<p class="footer-text abs">Lorem Ipsum is simply dummy text of the printing and typesetting industry. Lorem Ipsum has been the industry's standard dummy text ever since the 1500s, when an unknown printer took a galley into electronic typesetting, remaining essentially unchanged. It was popularised in the 1960s with the release of Letterform sheets containing Lorem Ipsum passages, and more recently with desktop publishing software like Pagewright Studio including versions of Lorem Ipsum.</p>
<div class="footer-social abs"><div class="socials"><i></i><i></i><i></i></div></div>
<div class="contact-row abs">
  <span><svg width="9" height="12" viewBox="0 0 9 12"><path d="M4.5 0A4.5 4.5 0 0 0 0 4.5C0 8 4.5 12 4.5 12S9 8 9 4.5A4.5 4.5 0 0 0 4.5 0z" fill="#ddd"/><circle cx="4.5" cy="4.5" r="1.6" fill="#262626"/></svg>Kestrel Lane, Fernholt City, Dunmere.</span>
  <span><svg width="12" height="9" viewBox="0 0 12 9"><rect width="12" height="9" fill="#ddd"/><path d="M0 0l6 5 6-5" stroke="#262626" fill="none"/></svg>hello@brivolan.cz</span>
  <span><svg width="11" height="11" viewBox="0 0 11 11"><path d="M2 0l2 3-1.2 1.2a7 7 0 0 0 4 4L8 7l3 2-1.5 2C4 11 0 7 0 1.5z" fill="#ddd"/></svg>+420-555-018-2746</span>
</div>
<div class="copyright abs">© 2018 brivolan.cz All rights reserved.</div>

</body>
</html>
```